Business cards for start-up accounting firm

I'm looking for a double sided business card ready for upload into Prontel ink or similar print providers with no modification required by me.
I'm looking for something simple as i think cards that are too 'busy' actually detract from the message. I have some thoughts but more than happy to see what comes up. The logo i have came out of left field and i love it the moment i saw it!

My thoughts:

Side 1: Just the logo, perhaps on a dark grey or charcoal background to make the logo colours stand out?

Side 2: The call to action from me website 'Looking for a more relaxed, friendly and interactive relationship with your accountant?' with my contact information
Name: Gavin Ormsby
Email: gavin@quellorix.com.au
Website: www.quellorix.com.au
Phone: 1300 742 916

The call to action needs to be the first thing they see when they look at side 2. If it helps to know what we do and how we do it there is a draft website at www.quellorix.com.au

Like i said, happy to consider anything that comes up :)

Target Market(s)

i'm targeting small business owners who experience a lot of stress around finacial reporting and have had bad experiences with accountants in the past.

Industry/Entity Type

Accounting

Contact Information for Business Card

Contained in the Description

Font styles to use
Serif
Sans Serif
Other font styles liked:
• See logo files attached

Colors
474747

Requirements
Must have
• My logo, slogan and contact information

```html
<!DOCTYPE html>
<html lang="en">
<head>
<meta charset="utf-8">
<title>Quellorix – Business Cards</title>
<link href="https://fonts.googleapis.com/css2?family=Fira+Sans:ital,wght@0,400;0,600;0,700;1,400&display=swap" rel="stylesheet">
<style>
  :root {
    --backdrop: #a7a7a9;
    --paper: #ebebee;
    --plum: #6e2c69;
    --gold: #d9b21d;
    --ink-soft: #7a6a78;
    --white: #f4f2f4;
  }
  * { box-sizing: border-box; margin: 0; padding: 0; }
  html, body { width: 1105px; height: 1200px; overflow: hidden; }
  body {
    background: var(--backdrop);
    font-family: "Fira Sans", sans-serif;
    position: relative;
  }
  .card {
    position: absolute;
    left: 182px;
    width: 746px;
    height: 427px;
    overflow: hidden;
  }
  .card--front { top: 119px; background: var(--paper); }
  .card--back { top: 637px; background: var(--plum); }

  .wordmark {
    position: absolute;
    left: 0; right: 0;
    text-align: center;
    font-weight: 700;
    letter-spacing: 1px;
  }
  .card--front .wordmark {
    top: 80px;
    font-size: 86px;
    line-height: 1;
    color: var(--plum);
  }
  .slogan {
    position: absolute;
    top: 198px;
    left: 0; right: 0;
    display: flex;
    justify-content: center;
    align-items: center;
    gap: 14px;
    font-size: 14px;
    letter-spacing: 2px;
    color: var(--ink-soft);
  }
  .slogan::before, .slogan::after {
    content: "";
    width: 38px;
    height: 1px;
    background: var(--ink-soft);
  }
  .holder-name {
    position: absolute;
    top: 258px;
    left: 0; right: 0;
    text-align: center;
    font-size: 38px;
    font-weight: 700;
    color: var(--plum);
  }
  .contact-band {
    position: absolute;
    left: 0; right: 0; bottom: 0;
    height: 83px;
    background: var(--plum);
    border-top: 3px solid var(--gold);
  }
  .contact {
    position: absolute;
    top: 0;
    transform: translateX(-50%);
    text-align: center;
    color: var(--white);
    font-size: 20px;
    white-space: nowrap;
  }
  .contact .icon {
    position: absolute;
    top: -21px;
    left: 50%;
    width: 36px;
    height: 36px;
    transform: translateX(-50%);
  }
  .contact--phone .icon { left: calc(50% - 12px); }
  .contact .value { display: block; padding-top: 30px; }
  .contact--phone { left: 111px; }
  .contact--email { left: 370px; }
  .contact--web { left: 619px; }

  .card--back .wordmark {
    top: 140px;
    font-size: 92px;
    line-height: 1;
    color: var(--white);
  }
  .call-to-action {
    position: absolute;
    top: 326px;
    left: 0; right: 0;
    text-align: center;
    font-style: italic;
    font-size: 20px;
    line-height: 29px;
    color: var(--white);
  }
</style>
</head>
<body>

<section class="card card--front" aria-label="Business card front">
  <div class="wordmark">Quellorix</div>
  <p class="slogan">CALM BOOKS, CLEAR GROWTH</p>
  <h1 class="holder-name">Gavin Ormsby</h1>
  <div class="contact-band">
    <div class="contact contact--phone">
      <svg class="icon" viewBox="0 0 36 36" aria-hidden="true">
        <circle cx="18" cy="18" r="17" fill="var(--gold)"/>
        <path d="M12 10c1-1 2-1 3 0l2 3c.6 1 .3 1.8-.5 2.4l-1 .8c.8 2 2.3 3.6 4.3 4.5l.8-1c.6-.8 1.5-1 2.4-.4l3 2c1 .7 1 1.9 0 2.8l-1.4 1.4c-1.3 1.2-3.5 1-6-.5-3.4-2-6.2-5-7.6-8.6-.8-2.2-.7-3.8.6-5z" fill="var(--plum)"/>
      </svg>
      <span class="value">1300 742 916</span>
    </div>
    <div class="contact contact--email">
      <svg class="icon" viewBox="0 0 36 36" aria-hidden="true">
        <circle cx="18" cy="18" r="17" fill="var(--gold)"/>
        <rect x="9" y="12" width="18" height="12" rx="1" fill="none" stroke="var(--plum)" stroke-width="2"/>
        <path d="M9.5 12.5 18 19l8.5-6.5" fill="none" stroke="var(--plum)" stroke-width="2"/>
      </svg>
      <span class="value">gavin@quellorix.com.au</span>
    </div>
    <div class="contact contact--web">
      <svg class="icon" viewBox="0 0 36 36" aria-hidden="true">
        <circle cx="18" cy="18" r="17" fill="var(--gold)"/>
        <circle cx="18" cy="18" r="9" fill="none" stroke="var(--plum)" stroke-width="2"/>
        <ellipse cx="18" cy="18" rx="4" ry="9" fill="none" stroke="var(--plum)" stroke-width="1.6"/>
        <path d="M9 18h18" stroke="var(--plum)" stroke-width="1.6"/>
      </svg>
      <span class="value">quellorix.com.au</span>
    </div>
  </div>
</section>

<section class="card card--back" aria-label="Business card back">
  <div class="wordmark">Quellorix</div>
  <p class="call-to-action">Looking for a more relaxed, friendly and<br>interactive relationship with your accountant?</p>
</section>

</body>
</html>
```